Design a business card
Business name: Kestrel Yield Consulting
Improving Business Profitibility

- An Overview of the Business & Service:

Business Performance Consulting

- The Target Market: Small to medium-sized business

- Design Specifics:
White card, blue ink, moon eclipse

No Logo

Target Market(s)

Small to medium-sized business

Font styles to use
Sans Serif

```html
<!DOCTYPE html>
<html lang="en">
<head>
<meta charset="utf-8">
<title>Kestrel Yield Consulting – Business Card</title>
<link href="https://fonts.googleapis.com/css2?family=Bebas+Neue&family=Open+Sans:wght@400;600&display=swap" rel="stylesheet">
<style>
  :root {
    --backdrop: #2a2a2a;
    --card-white: #eeeeee;
    --card-black: #000000;
    --ink-blue: #2e6db4;
    --ink-dark: #333333;
    --rule-grey: #a8a8a8;
    --tagline: #e8e8e8;
    --photo-fill: #7a3418;
  }
  html, body {
    margin: 0;
    padding: 0;
    width: 1200px;
    height: 1200px;
    overflow: hidden;
    background: var(--backdrop);
  }
  .canvas {
    position: relative;
    width: 1200px;
    height: 1200px;
  }
  .card {
    position: absolute;
    top: 310px;
    box-shadow: 2px 3px 6px rgba(0,0,0,0.5);
  }
  .card-front {
    left: 234px;
    width: 364px;
    height: 594px;
    background: var(--card-white);
    text-align: center;
    font-family: "Open Sans", sans-serif;
    color: var(--ink-dark);
  }
  .card-back {
    left: 627px;
    width: 370px;
    height: 596px;
    background: var(--card-black);
  }
  .company-name {
    position: absolute;
    left: 0;
    right: 0;
    top: 157px;
    margin: 0;
    font-family: "Bebas Neue", sans-serif;
    font-weight: 400;
    color: var(--ink-blue);
    line-height: 1;
  }
  .company-name .line-main {
    display: block;
    font-size: 43px;
  }
  .company-name .line-sub {
    display: flex;
    align-items: center;
    justify-content: center;
    gap: 8px;
    font-size: 37px;
    margin-top: -4px;
  }
  .company-name .line-sub::before,
  .company-name .line-sub::after {
    content: "";
    width: 68px;
    height: 3px;
    background: var(--ink-blue);
  }
  .person {
    position: absolute;
    left: 0;
    right: 0;
    top: 330px;
  }
  .person-name {
    margin: 0;
    font-family: "Bebas Neue", sans-serif;
    font-weight: 400;
    font-size: 31px;
    line-height: 1;
    color: var(--ink-blue);
  }
  .person-role {
    margin: -2px 0 0;
    font-size: 17px;
    line-height: 1.2;
  }
  .rule {
    width: 208px;
    height: 1px;
    margin: 7px auto 8px;
    background: var(--rule-grey);
  }
  .rule-lower { margin: 10px auto 7px; }
  .contact-list {
    list-style: none;
    margin: 0;
    padding: 0;
    font-size: 17px;
    line-height: 21.5px;
  }
  .contact-list .label { color: var(--ink-blue); font-weight: 600; }
  .contact-list .web { color: var(--ink-blue); font-weight: 600; }
  .address {
    margin: 0;
    font-size: 17px;
    line-height: 21.5px;
    font-style: normal;
  }
  .eclipse-photo {
    position: absolute;
    left: 100px;
    top: 202px;
    width: 180px;
    height: 180px;
    background: var(--photo-fill);
  }
  .tagline {
    position: absolute;
    left: 0;
    right: 0;
    top: 524px;
    margin: 0;
    text-align: center;
    font-family: "Open Sans", sans-serif;
    font-size: 16px;
    letter-spacing: 0.2px;
    color: var(--tagline);
  }
</style>
</head>
<body>
<div class="canvas">
  <section class="card card-front">
    <h1 class="company-name">
      <span class="line-main">Kestrel Yield</span>
      <span class="line-sub">Consulting</span>
    </h1>
    <div class="person">
      <h2 class="person-name">Marcus Ellery</h2>
      <p class="person-role">Managing Director</p>
      <div class="rule"></div>
      <ul class="contact-list">
        <li><span class="label">P:</span> 044-987 654 321</li>
        <li><span class="label">M:</span> 044-987 654 321</li>
        <li><span class="label">E:</span> info@kestrelyield.com</li>
        <li class="web">www.kestrelyield.com</li>
      </ul>
      <div class="rule rule-lower"></div>
      <address class="address">48, Harbour Lane<br>Northfield, 604512.</address>
    </div>
  </section>

  <section class="card card-back">
    <div class="eclipse-photo" role="img" aria-label="Photograph of a red lunar eclipse against a black night sky"></div>
    <p class="tagline">IMPROVING BUSINESS PROFITIBILITY</p>
  </section>
</div>
</body>
</html>
```